New Business Card for Web Design/Internet Marketing Company

Looking for a great looking new business card. We are a 10 year old web design, internet marketing and website management company that works mostly with small businesses.

Our new card needs to better match the colors and style of our website, be bold, extremely usable and slightly edgy.

Target Market(s)

Small/Medium businesses that have websites

Industry/Entity Type

Internet

Requirements
Must have
• Front and back design, full color, rounded corners please

Must use the colors/style of our website (JPG provided)

INFO FOR CARDS (as readable as possible please)
Mark Pellow
President/CEO
mark@brightlanesites.com
Phone: 520-481-7093
Toll Free: 866-481-7093
Address: 4315 E. Kestrel Ave. Ste. 140, Tucson, AZ 85733

THINGS I WANT TO PROMOTE (if there is room):
1. Our Website - www.brightlanesites.com

2. Social Media
Twitter: @brightlanesites
Facebook: www.facebook.com/brightlanesites

3. Our Services
Web Design
Internet Marketing
Website Management

```html
<!DOCTYPE html>
<html lang="en">
<head>
<meta charset="utf-8">
<title>Brightlane Sites – Business Card</title>
<link rel="stylesheet" href="https://fonts.googleapis.com/css2?family=Cabin:ital,wght@0,400;0,600;0,700;1,400&display=swap">
<style>
  :root {
    --stage: #2e2f31;
    --navy-deep: #10304f;
    --navy-mid: #135a86;
    --navy-glow: #1577a8;
    --orange: #f07c2c;
    --orange-deep: #de611c;
    --white: #ffffff;
    --ink-soft: #e6eef5;
    --icon: #8fb4d3;
  }
  * { box-sizing: border-box; margin: 0; padding: 0; }
  html, body {
    width: 1200px; height: 800px; overflow: hidden;
    background: var(--stage);
    font-family: "Cabin", "Trebuchet MS", sans-serif;
  }
  .canvas { position: relative; width: 1200px; height: 800px; }

  .card {
    position: absolute;
    width: 540px; height: 300px;
    border-radius: 28px;
    overflow: hidden;
    box-shadow: 0 10px 28px rgba(0,0,0,.45);
  }
  .card--front { left: 50px; top: 90px; }
  .card--back  { left: 610px; top: 410px; }

  .card__art { position: absolute; inset: 0; width: 100%; height: 100%; }

  .brand {
    position: absolute;
    display: flex; align-items: center; gap: 12px;
    color: var(--orange);
    font-weight: 600;
    white-space: nowrap;
  }
  .brand__dot {
    border-radius: 50%;
    background: var(--orange);
  }
  .card--front .brand { left: 0; right: 0; top: 68px; justify-content: center; font-size: 46px; }
  .card--front .brand__dot { width: 40px; height: 40px; }
  .card--back .brand { left: 24px; top: 22px; font-size: 25px; gap: 8px; }
  .card--back .brand__dot { width: 24px; height: 24px; }

  .web-address {
    position: absolute; left: 0; right: 0;
    text-align: center;
    color: var(--white);
    font-style: italic;
    letter-spacing: 2.5px;
  }
  .card--front .web-address { bottom: 24px; font-size: 27px; }
  .card--back .web-address { bottom: 22px; font-size: 25px; }

  .person { position: absolute; left: 28px; top: 78px; color: var(--white); }
  .person__name { font-size: 22px; font-weight: 700; letter-spacing: .3px; }
  .person__title { font-size: 12px; margin-top: 4px; color: var(--ink-soft); }

  .social { position: absolute; left: 26px; top: 160px; list-style: none; color: var(--ink-soft); font-size: 12.5px; }
  .social li { display: flex; align-items: center; gap: 8px; margin-bottom: 7px; }
  .social__mark { width: 15px; height: 15px; border-radius: 3px; background: var(--icon); }

  .contact {
    position: absolute; right: 28px; top: 92px;
    text-align: right; color: var(--ink-soft);
    font-size: 13px; line-height: 1.4;
    font-style: normal;
  }
  .contact__group + .contact__group { margin-top: 14px; }
</style>
</head>
<body>
<main class="canvas">

  <section class="card card--front" aria-label="Business card front">
    <svg class="card__art" viewBox="0 0 540 300" preserveAspectRatio="none" aria-hidden="true">
      <defs>
        <radialGradient id="frontGlow" cx="45%" cy="35%" r="70%">
          <stop offset="0" stop-color="#1577a8"/>
          <stop offset=".55" stop-color="#135a86"/>
          <stop offset="1" stop-color="#10304f"/>
        </radialGradient>
        <linearGradient id="frontBand" x1="0" y1="0" x2="0" y2="1">
          <stop offset="0" stop-color="#f58a38"/>
          <stop offset="1" stop-color="#de611c"/>
        </linearGradient>
      </defs>
      <rect width="540" height="300" fill="url(#frontGlow)"/>
      <path d="M0 200 Q250 158 540 192 L540 300 L0 300 Z" fill="#0b2740" opacity=".45"/>
      <path d="M0 208 Q250 166 540 198 L540 300 L0 300 Z" fill="url(#frontBand)"/>
    </svg>
    <div class="brand"><span class="brand__dot"></span>Brightlane Sites</div>
    <p class="web-address">www.brightlanesites.com</p>
  </section>

  <section class="card card--back" aria-label="Business card back">
    <svg class="card__art" viewBox="0 0 540 300" preserveAspectRatio="none" aria-hidden="true">
      <defs>
        <radialGradient id="backGlow" cx="50%" cy="45%" r="70%">
          <stop offset="0" stop-color="#1577a8"/>
          <stop offset=".55" stop-color="#135a86"/>
          <stop offset="1" stop-color="#10304f"/>
        </radialGradient>
        <linearGradient id="backBand" x1="0" y1="0" x2="0" y2="1">
          <stop offset="0" stop-color="#f58a38"/>
          <stop offset="1" stop-color="#de611c"/>
        </linearGradient>
      </defs>
      <rect width="540" height="300" fill="url(#backGlow)"/>
      <path d="M0 222 Q260 186 540 214 L540 300 L0 300 Z" fill="#0b2740" opacity=".45"/>
      <path d="M0 230 Q260 194 540 221 L540 300 L0 300 Z" fill="url(#backBand)"/>
    </svg>

    <div class="brand"><span class="brand__dot"></span>Brightlane Sites</div>

    <div class="person">
      <h1 class="person__name">Mark Pellow</h1>
      <p class="person__title">President/CEO</p>
    </div>

    <ul class="social">
      <li><span class="social__mark"></span>friendhub.net/brightlanesites</li>
      <li><span class="social__mark"></span>@brightlanesites</li>
    </ul>

    <address class="contact">
      <div class="contact__group">
        <p>Address: 4315 E. Kestrel Ave.</p>
        <p>Ste. 140, Tucson, AZ 85733</p>
      </div>
      <div class="contact__group">
        <p>Phone: 520-481-7093</p>
        <p>Toll Free: 866-481-7093</p>
        <p>mark@brightlanesites.com</p>
      </div>
    </address>

    <p class="web-address">www.brightlanesites.com</p>
  </section>

</main>
</body>
</html>
```